Tidy Acres Complete Garden & Lawn Care

I will upload a flyer, I wanna pretty much same, please change the logo and I will upload description of the job I offer soon
Gonna be in A5 size, and I would like like double sides
I would like something creative and modern to impress the clients, I upload my business card as well, on flyer need to have my business card information
BRILKOR IS ONLY A SAMPLE FLYER AND PLEASE I DONT WANT TO SEE IT IN MY FLYERS, Thanks
Updates
on small lines instead of 6 months I would like 3 months
Target Market(s)
Residentials and commercials
Industry/Entity Type
Business
Look and feel
Each slider illustrates characteristics of the customer's brand and the style your logo design should communicate.

```html
<!DOCTYPE html>
<html lang="en">
<head>
<meta charset="utf-8">
<title>Tidy Acres – Flyer</title>
<link rel="stylesheet" href="https://fonts.googleapis.com/css2?family=Cinzel:wght@700&family=Ubuntu:wght@500&family=Open+Sans:wght@400&display=swap">
<style>
  :root {
    --lime-glow: #f2ffd6;
    --lime-light: #b8ee5a;
    --green-main: #5cc91f;
    --green-mid: #3fae14;
    --green-deep: #1f7d0c;
    --brand-green: #2f8f1c;
    --white: #ffffff;
  }
  html, body {
    margin: 0;
    padding: 0;
    overflow: hidden;
    background: #e9eee6;
  }
  .flyer {
    position: relative;
    width: 846px;
    height: 1200px;
    overflow: hidden;
    background:
      radial-gradient(ellipse 70% 45% at 70% 8%, var(--lime-glow) 0%, var(--lime-light) 45%, rgba(184,238,90,0) 100%),
      linear-gradient(180deg, #8fdc3a 0%, var(--green-main) 45%, var(--green-mid) 100%);
  }
  .flyer__waves {
    position: absolute;
    inset: 0;
    width: 846px;
    height: 1200px;
  }
  .brand__mark {
    position: absolute;
    top: 40px;
    left: 333px;
    width: 180px;
    height: 180px;
    border-radius: 50%;
    background: var(--brand-green);
  }
  .brand {
    position: absolute;
    top: 262px;
    left: 0;
    width: 846px;
    text-align: center;
    color: var(--brand-green);
    font-family: "Ubuntu", sans-serif;
    font-weight: 500;
  }
  .brand__name {
    margin: 0;
    font-size: 66px;
    letter-spacing: 6px;
    line-height: 1;
  }
  .brand__tagline {
    margin: 20px 0 0;
    font-size: 31px;
    letter-spacing: 3px;
    line-height: 1;
  }
  .headline {
    position: absolute;
    top: 594px;
    left: 0;
    width: 846px;
    margin: 0;
    text-align: center;
    color: var(--white);
    font-family: "Cinzel", serif;
    font-weight: 700;
    font-size: 86px;
    line-height: 102px;
    letter-spacing: 2px;
  }
  .contact {
    position: absolute;
    left: 26px;
    bottom: 14px;
    margin: 0;
    color: var(--white);
    font-family: "Open Sans", sans-serif;
    font-size: 27px;
    line-height: 37px;
    letter-spacing: 0.5px;
  }
  .contact p { margin: 0; }
</style>
</head>
<body>
<div class="flyer">
  <svg class="flyer__waves" viewBox="0 0 846 1200" aria-hidden="true">
    <defs>
      <linearGradient id="footerGrad" x1="0" y1="0" x2="0" y2="1">
        <stop offset="0" stop-color="#3aa812"/>
        <stop offset="1" stop-color="#1f7d0c"/>
      </linearGradient>
      <linearGradient id="swoosh" x1="0" y1="0" x2="1" y2="0">
        <stop offset="0" stop-color="#ffffff" stop-opacity="0.1"/>
        <stop offset="0.5" stop-color="#f4ffd8" stop-opacity="0.85"/>
        <stop offset="1" stop-color="#ffffff" stop-opacity="0.2"/>
      </linearGradient>
    </defs>
    <path d="M0 395 C200 430 420 470 846 420" fill="none" stroke="#ffffff" stroke-opacity="0.45" stroke-width="3"/>
    <path d="M0 410 C220 450 460 490 846 455" fill="none" stroke="#ffffff" stroke-opacity="0.3" stroke-width="2"/>
    <path d="M0 470 C250 440 560 520 846 480" fill="none" stroke="#ffffff" stroke-opacity="0.18" stroke-width="2"/>
    <path d="M0 520 C300 480 560 560 846 520" fill="none" stroke="#ffffff" stroke-opacity="0.12" stroke-width="2"/>
    <path d="M0 560 C260 540 600 600 846 560 L846 600 C600 640 260 580 0 600 Z" fill="#ffffff" fill-opacity="0.06"/>
    <path d="M0 960 C220 900 520 990 846 930 L846 1200 L0 1200 Z" fill="#6fd22a" fill-opacity="0.6"/>
    <path d="M0 1010 C260 970 560 1020 846 975 L846 1200 L0 1200 Z" fill="url(#footerGrad)"/>
    <path d="M0 1005 C260 962 560 1012 846 968 L846 985 C560 1030 260 985 0 1022 Z" fill="url(#swoosh)"/>
    <path d="M0 1040 C300 1010 580 1060 846 1020" fill="none" stroke="#ffffff" stroke-opacity="0.25" stroke-width="2"/>
  </svg>

  <div class="brand__mark" role="img" aria-label="Tidy Acres brand mark"></div>

  <div class="brand">
    <p class="brand__name">TIDY ACRES</p>
    <p class="brand__tagline">COMPLETE GARDEN &amp; LAWN CARE</p>
  </div>

  <h1 class="headline">YOUR LAWN<br>OUR CARE</h1>

  <div class="contact">
    <p>Daniel / Marcus</p>
    <p>Phone: 0400 555 274</p>
    <p>Email:hello@tidyacres.example</p>
  </div>
</div>
</body>
</html>
```